Brevanta Interiors
Business Card, Stationery Package, Email Signature
Project: Brevanta Interiors
Brevanta Interiors -
Creative Brief
Professional
Marisol Pryde
Managing Director
P.O.Box 4372 Harrowvale, QX 00000 - 4372
mpryde@brevantainteriors.example
www.brevantainteriors.example
Brevanta Interiors is a retail store offering Flooring products and Installation services. We would like to have the following items made: Business Card, Stationery Package (Fax, Letterhead, Envelopes, etc.), and Email Signature. We would like to see two types of fonts created for comparison, the original font and one of your own professional choices. Winner, please provide all design templates for future modification upon completion of the contest. Thank you!
logo, text, slogan, and web address.

```html
<!DOCTYPE html>
<html lang="en">
<head>
<meta charset="utf-8">
<title>Brevanta Interiors Stationery</title>
<link href="https://fonts.googleapis.com/css2?family=Open+Sans:wght@400;600;700&display=swap" rel="stylesheet">
<style>
:root{
  --bg:#e9e6e2;
  --paper:#ffffff;
  --navy:#1d3b8c;
  --green:#2a9d57;
  --teal:#1f7f8f;
  --ink:#3c4250;
  --muted:#8a909c;
  --faint:#e4ece9;
  --line:#d5d8de;
  --shadow:rgba(0,0,0,.22);
}
*{margin:0;padding:0;box-sizing:border-box}
html,body{width:1200px;height:307px;overflow:hidden;background:var(--bg);font-family:"Open Sans",Arial,sans-serif;color:var(--ink)}
.canvas{position:relative;width:1200px;height:307px}
.item{position:absolute;background:var(--paper);box-shadow:0 2px 4px var(--shadow);overflow:hidden}
.brand{display:flex;align-items:center;gap:3px;font-weight:700;color:var(--navy);white-space:nowrap;font-size:6px}
.brand .dot{width:7px;height:7px;background:var(--green);border-radius:50%;flex:none}
.swoosh{position:absolute;width:100%;height:100%;left:0;top:0}
.small{font-size:4px;line-height:5.5px;color:var(--muted);white-space:nowrap}
.caption{position:absolute;font-size:5px;color:var(--muted);text-align:center}
.watermark{position:absolute;left:0;right:0;text-align:center;font-weight:700;color:var(--faint);font-size:13px}

.logo-sample{position:absolute;left:14px;top:30px;width:160px}
.logo-sample .brand{font-size:13px}
.logo-sample .brand .dot{width:13px;height:13px}
.logo-sample .tag{font-size:6px;color:var(--green);margin-top:3px;letter-spacing:.5px}

.card{width:120px;height:52px}
.card .brand{position:absolute;left:6px;top:6px}
.card .details{position:absolute;left:6px;top:18px}
.card.flipped .brand,.card.flipped .details{left:38px}
.card .name{font-size:5px;font-weight:700;color:var(--navy)}
.card .centered{position:absolute;left:0;right:0;top:22px;justify-content:center}

.comp{left:188px;top:8px;width:100px;height:82px}
.comp .brand{position:absolute;left:6px;top:8px}
.comp .details{position:absolute;left:6px;top:22px}

.letterhead{top:8px;width:180px;height:292px}
.letterhead .brand{position:absolute;left:28px;top:14px;font-size:7px}
.letterhead .addr{position:absolute;left:108px;top:12px}
.letterhead .watermark{top:122px}

.envelope{left:698px;width:190px}
.envelope .brand{position:absolute;left:10px;top:10px}
.envelope .from{position:absolute;left:10px;top:21px}
.envelope .watermark{top:40%}

.stack .env{position:absolute;width:260px;height:72px;box-shadow:0 2px 5px var(--shadow)}
.env.green{background:var(--green)}
.env.white{background:var(--paper)}
.env .brand{position:absolute;left:0;right:0;top:36px;justify-content:center}
.flap{position:absolute;left:0;top:0;width:100%;height:100%}
</style>
</head>
<body>
<main class="canvas">

  <section class="logo-sample">
    <div class="brand"><span class="dot"></span>Brevanta Interiors</div>
    <div class="tag">FLOORING &amp; INSTALLATION</div>
  </section>

  <section class="item comp">
    <div class="brand"><span class="dot"></span>Brevanta Interiors</div>
    <div class="details small">P.O.Box 4372 Harrowvale, QX 00000 - 4372<br>Tel (000) 555-0147<br>Fax (000) 555-0148<br>www.brevantainteriors.example</div>
  </section>

  <section class="item card" style="left:19px;top:180px">
    <svg class="swoosh" viewBox="0 0 120 52" preserveAspectRatio="none"><path d="M90 52 Q110 40 120 20 L120 52Z" fill="var(--navy)"/><path d="M84 52 Q106 42 120 16 L120 20 Q110 40 90 52Z" fill="var(--green)"/></svg>
    <div class="brand"><span class="dot"></span>Brevanta Interiors</div>
    <div class="details small"><span class="name">Marisol Pryde</span><br>Managing Director<br>mpryde@brevantainteriors.example</div>
  </section>
  <section class="item card flipped" style="left:149px;top:180px">
    <svg class="swoosh" viewBox="0 0 120 52" preserveAspectRatio="none"><path d="M0 0 L30 0 Q10 10 0 30Z" fill="var(--navy)"/><path d="M30 0 L36 0 Q12 12 0 36 L0 30 Q10 10 30 0Z" fill="var(--green)"/></svg>
    <div class="brand"><span class="dot"></span>Brevanta Interiors</div>
    <div class="details small"><span class="name">Marisol Pryde</span><br>P.O.Box 4372<br>www.brevantainteriors.example</div>
  </section>
  <section class="item card" style="left:19px;top:243px">
    <svg class="swoosh" viewBox="0 0 120 52" preserveAspectRatio="none"><path d="M0 0 L30 0 Q10 10 0 30Z" fill="var(--navy)"/></svg>
    <div class="brand centered"><span class="dot"></span>Brevanta Interiors</div>
  </section>
  <section class="item card" style="left:149px;top:243px">
    <svg class="swoosh" viewBox="0 0 120 52" preserveAspectRatio="none"><path d="M90 52 Q110 40 120 20 L120 52Z" fill="var(--navy)"/></svg>
    <div class="brand centered"><span class="dot"></span>Brevanta Interiors</div>
  </section>

  <section class="item letterhead" style="left:300px">
    <svg class="swoosh" viewBox="0 0 180 292" preserveAspectRatio="none"><path d="M0 0 L22 0 Q6 10 0 40Z" fill="var(--navy)"/><path d="M22 0 L28 0 Q8 14 0 48 L0 40 Q6 10 22 0Z" fill="var(--green)"/><path d="M180 292 L150 292 Q174 280 180 250Z" fill="var(--navy)"/></svg>
    <div class="brand"><span class="dot"></span>Brevanta Interiors</div>
    <div class="addr small">P.O.Box 4372<br>Harrowvale, QX 00000<br>www.brevantainteriors.example</div>
    <div class="watermark">Brevanta Interiors</div>
  </section>
  <section class="item letterhead" style="left:492px">
    <svg class="swoosh" viewBox="0 0 180 292" preserveAspectRatio="none"><path d="M0 0 L22 0 Q6 10 0 40Z" fill="var(--navy)"/><path d="M180 292 L150 292 Q174 280 180 250Z" fill="var(--navy)"/><path d="M144 292 L150 292 Q174 280 180 250 L180 242 Q172 278 144 292Z" fill="var(--green)"/></svg>
    <div class="brand"><span class="dot"></span>Brevanta Interiors</div>
    <div class="addr small">P.O.Box 4372<br>Harrowvale, QX 00000<br>www.brevantainteriors.example</div>
    <div class="watermark">Brevanta Interiors</div>
  </section>
  <div class="caption" style="left:300px;top:301px;width:180px">Letterhead</div>
  <div class="caption" style="left:492px;top:301px;width:180px">Letterhead</div>

  <section class="item envelope" style="top:65px;height:98px">
    <svg class="swoosh" viewBox="0 0 190 98" preserveAspectRatio="none"><path d="M0 0 L24 0 Q6 8 0 30Z" fill="var(--navy)"/></svg>
    <div class="brand"><span class="dot"></span>Brevanta Interiors</div>
    <div class="from small">P.O.Box 4372 Harrowvale, QX 00000 - 4372</div>
    <div class="watermark">Brevanta Interiors</div>
  </section>
  <section class="item envelope" style="top:180px;height:100px">
    <svg class="swoosh" viewBox="0 0 190 100" preserveAspectRatio="none"><path d="M0 0 L24 0 Q6 8 0 30Z" fill="var(--navy)"/><path d="M24 0 L30 0 Q8 10 0 36 L0 30 Q6 8 24 0Z" fill="var(--green)"/></svg>
    <div class="brand"><span class="dot"></span>Brevanta Interiors</div>
    <div class="from small">P.O.Box 4372 Harrowvale, QX 00000 - 4372</div>
    <div class="watermark">Brevanta Interiors</div>
  </section>
  <div class="caption" style="left:698px;top:164px;width:190px">Envelope</div>
  <div class="caption" style="left:698px;top:282px;width:190px">Envelope</div>

  <section class="stack">
    <div class="env green" style="left:922px;top:48px">
      <svg class="flap" viewBox="0 0 260 72" preserveAspectRatio="none"><path d="M0 0 L130 40 L260 0Z" fill="var(--teal)"/></svg>
    </div>
    <div class="env white" style="left:920px;top:130px">
      <svg class="flap" viewBox="0 0 260 72" preserveAspectRatio="none"><path d="M0 0 L130 34 L260 0Z" fill="var(--navy)"/></svg>
    </div>
    <div class="env white" style="left:916px;top:200px">
      <svg class="flap" viewBox="0 0 260 72" preserveAspectRatio="none"><path d="M0 0 L130 30 L260 0" fill="none" stroke="var(--line)" stroke-width="1"/></svg>
      <div class="brand"><span class="dot"></span>Brevanta Interiors</div>
    </div>
  </section>

</main>
</body>
</html>
```